Marevanga Wines

A Red Wine Label for future Wine Concept called Marevanga Wine. The back label will have the following words which capture the essence of the wine "I am sworn to the secrecy about the origins of this wine but I can assure you it’s from the best cellars of Africa. Marevanga is an African (Shona) name which loosely means honour, praise or to be held in high exteem. Hold on to your hats because this wine is a whirlwind of flavours. It's dark, spicy and fruity flavours will attack the palate with warm aggression and intent whilst being served with Sadza/ Nsima and roasted beef accompanied with mufushwa (dried vegetables) cooked in grounded nut paste. The inspiring flame, style and mood of an African braai, together with its outlandish flavours popping in and out of the glass, Marevanga will make every serving a gesture of respect and distinction!!!"
Updates

I will be buying wine packed in unbranded bottles then Brand it as Marevanga on my own Marevanga label for some African event theme. The wines will be South African a Shiraz. So I need a back label with message placed in brief and front label for a red wine bottle. I have attached some old labels for the wine so I need a redesign of the l label for have a morden and African feel to it                                   

Please

Target Market(s)

Appeal to general populace and those with an afrocentric feel

Requirements
Must have
• Back and front labels, simplicity
Should not have
• Too many colours

```html
<!DOCTYPE html>
<html lang="en">
<head>
<meta charset="utf-8">
<title>Marevanga Shiraz – Front and Back Labels</title>
<link rel="stylesheet" href="https://fonts.googleapis.com/css2?family=Montserrat:wght@700&family=PT+Sans+Narrow:wght@400;700&display=swap">
<style>
  :root {
    --stage-light: #d9d9d9;
    --stage-dark: #6b6b6b;
    --label-paper: #a39c99;
    --label-paper-light: #aaa4a1;
    --frame-brown: #3a2417;
    --ink: #1f1a17;
    --art-brown: #7a4a24;
    --art-tan: #b98a5a;
    --art-dark: #4a2a14;
  }
  * { box-sizing: border-box; margin: 0; padding: 0; }
  html, body { width: 1200px; height: 1000px; overflow: hidden; }
  body {
    position: relative;
    background: linear-gradient(90deg, var(--stage-dark) 0%, var(--stage-light) 45%, var(--stage-dark) 100%);
    font-family: "PT Sans Narrow", "Arial Narrow", sans-serif;
    color: var(--ink);
  }
  .label {
    position: absolute;
    background: linear-gradient(180deg, var(--label-paper-light), var(--label-paper));
  }
  .label__frame {
    position: absolute;
    inset: 22px;
    border: 3px solid var(--frame-brown);
  }
  .label > .abs { position: absolute; left: 0; right: 0; text-align: center; }
  .brand-name {
    font-family: "Montserrat", "Arial", sans-serif;
    font-weight: 700;
    font-size: 34px;
    letter-spacing: 2px;
    line-height: 1;
  }
  .vintage { font-size: 26px; line-height: 1; }
  .varietal { font-weight: 700; font-size: 30px; line-height: 1; }
  .origin { font-weight: 700; font-size: 19px; line-height: 1; }
  .measure { font-size: 22px; line-height: 1.15; }
  .art {
    position: absolute;
    border-radius: 4px;
  }
  .art--mask {
    background: radial-gradient(ellipse at 50% 45%, var(--art-tan) 0%, var(--art-brown) 60%, var(--art-dark) 100%);
    border-radius: 48% 48% 44% 44%;
  }
  .art--zigzag-column {
    background: linear-gradient(90deg, var(--art-dark), var(--art-brown), var(--art-dark));
    opacity: .8;
  }
  .art--zigzag-band {
    background: linear-gradient(180deg, var(--art-dark), var(--art-brown), var(--art-dark));
    opacity: .8;
  }
  .warning {
    position: absolute;
    left: 37px;
    right: 37px;
    top: 244px;
    font-size: 14px;
    line-height: 1.3;
    text-align: justify;
    text-transform: uppercase;
  }

  .label--front { left: 150px; top: 177px; width: 421px; height: 646px; }
  .label--back  { left: 620px; top: 258px; width: 431px; height: 484px; }
</style>
</head>
<body>

  <section class="label label--front" aria-label="Front label">
    <div class="label__frame"></div>
    <h1 class="abs brand-name" style="top:67px">MAREVANGA</h1>
    <p class="abs vintage" style="top:120px">2005</p>
    <div class="art art--zigzag-column" style="left:34px; top:132px; width:37px; height:373px" role="img" aria-label="Vertical African zigzag ornament"></div>
    <div class="art art--zigzag-column" style="left:344px; top:132px; width:40px; height:373px" role="img" aria-label="Vertical African zigzag ornament"></div>
    <div class="art art--mask" style="left:144px; top:161px; width:162px; height:284px" role="img" aria-label="Illustration of a carved African tribal mask"></div>
    <p class="abs varietal" style="top:463px">SHIRAZ</p>
    <p class="abs origin" style="top:502px">SOUTH AFRICA</p>
    <p class="abs measure" style="top:541px">13.5% vol<br>750ml</p>
  </section>

  <section class="label label--back" aria-label="Back label">
    <div class="label__frame"></div>
    <h2 class="abs brand-name" style="top:52px">MAREVANGA</h2>
    <div class="art art--zigzag-band" style="left:62px; top:156px; width:332px; height:28px" role="img" aria-label="Horizontal African zigzag ornament"></div>
    <div class="art art--mask" style="left:179px; top:88px; width:90px; height:150px" role="img" aria-label="Illustration of a carved African tribal mask"></div>
    <p class="vintage" style="position:absolute; left:285px; top:102px">2005</p>
    <p class="warning">"Government warning:" "(1) According to the Surgeon General, women should not drink alcoholic beverages during pregnancy because of the risk of birth defects. (2) Consumption of alcoholic beverages impairs your ability to drive a car or operate machinery, and may cause health problems."</p>
    <p class="abs origin" style="top:378px">SOUTH AFRICA</p>
    <p class="abs measure" style="top:402px">13.5% vol&nbsp;&nbsp;&nbsp;750ml</p>
  </section>

</body>
</html>
```